Velvet Fern Tagline: Beauty & Balance

I’m looking to create a professional website for my body sculpting, facial, waxing, and wellness spa. I’d like clarity on all required components and integrations needed for a fully functional, client‑friendly platform.**

The website should include:

- **Home Page**
- **About Page**
- **Contact Page**
- **Services Page** (with detailed service descriptions)
- **Meet the Team Page**
- **Product Page** (with e‑commerce capabilities)
- **Blog Section** (multiple posts/pages)
**** Education-
- **Refund & Cancellation Policies Page, Legal Polices ( to discuss potient risk when using products and equipment for services rendered *

**Functionality Requirements: **

- Seamless **integration with external platforms** used for scheduling, client management, or marketing.
- Full **e‑commerce capability**, including:
- “Buy Now” Pay Later” solutions like Pay-Lattice, Vorsta, Quillow and Integration with **Tindle Payments** and similar financing providers
- Ability to manage and sell both **services and retail products**.
- A user‑friendly backend for updating content, products, and blog posts.

Technical Requirements
• HIPAA Compliance: Use platforms like Mavrelo or ClinivaHub to ensure client health data and photos are stored securely. HIPAA Notice: Since you offer post-op services, include a small disclaimer below your contact form: "Please do not share sensitive medical information through this form. Private health details will be collected during your secure, HIPAA-compliant intake process".

• Mobile Optimization: Ensure the site is "responsive" so it looks perfect on smartphones where most clients will book.
• SEO: Include local keywords like "Sacramento Body Sculpting" and "Best Waxing in 95731" to help people find you.

I’m seeking guidance on what is required to build this site effectively, including platform recommendations, integrations, and any technical considerations.

Velvet Fern
Tagline : Beauty and Balance

Logo- I created this logo attached. I want this concept but want it revised properly and I am willing to pay for a revised logo which will not be too far off from what you currently see.

Beauty, Cosmetic, Spa, Wellness, Holistic

```html
<!DOCTYPE html>
<html lang="en">
<head>
<meta charset="utf-8">
<title>Velvet Fern — Beauty &amp; Balance</title>
<link rel="stylesheet" href="https://fonts.googleapis.com/css2?family=Cinzel:wght@600;700&family=Montserrat:wght@400;500;600;700&display=swap">
<style>
:root{
  --plum:#8a2876;
  --plum-deep:#6b1d5c;
  --magenta:#b23a8c;
  --gold:#d9a23a;
  --gold-light:#f1cf7a;
  --gold-deep:#b97f22;
  --teal:#22b3a0;
  --green:#3cbf7a;
  --cream:#fbf6ee;
  --white:#ffffff;
  --ink:#3b2a36;
  --muted:#7d6d78;
  --canvas:#e7e6ea;
  --head:"Cinzel", Georgia, serif;
  --body:"Montserrat", Arial, sans-serif;
}
*{box-sizing:border-box;margin:0;padding:0}
html,body{width:1200px;height:2232px;overflow:hidden}
body{background:var(--canvas);font-family:var(--body);color:var(--ink);position:relative}
.page{position:absolute;top:16px;width:568px;background:var(--white);box-shadow:0 2px 10px rgba(0,0,0,.12);overflow:hidden}
.page--home{left:20px}
.page--alt{left:612px}
section,header,footer{position:relative;overflow:hidden}
.photo{border-radius:6px}
.wave{position:absolute;left:0;width:100%;display:block}
.wave--top{top:0}
.wave--bottom{bottom:0}

/* navigation */
.site-nav{height:40px;display:flex;align-items:center;justify-content:space-between;padding:0 16px;background:var(--white);border-bottom:3px solid var(--plum)}
.site-nav__contact{font-size:7px;color:var(--plum);display:flex;gap:10px}
.site-nav__menu{display:flex;gap:10px;font-size:7px;font-weight:700;color:var(--plum);align-items:center}
.btn{display:inline-block;font-family:var(--body);font-weight:700;font-size:8px;letter-spacing:.06em;color:var(--white);background:var(--gold);border-radius:12px;padding:5px 14px;text-transform:uppercase}
.btn--plum{background:var(--plum)}
.btn--small{font-size:6px;padding:3px 9px}

/* hero */
.hero{height:240px;background:linear-gradient(100deg,#4a2a1e 0%,#9c6a4c 40%,#e2c1a4 70%,#c9a688 100%)}
.hero__text{position:absolute;left:30px;top:52px;z-index:2}
.hero__title{font-family:var(--head);font-weight:700;color:var(--white);font-size:22px;line-height:1.15;text-shadow:0 1px 3px rgba(0,0,0,.4)}
.hero__title .accent{color:var(--gold-light)}
.hero .btn{margin-top:14px}

/* headings */
.section-title{font-family:var(--head);font-weight:700;text-align:center;color:var(--plum);font-size:19px;letter-spacing:.04em}
.section-title--light{color:var(--white)}
.text-small{font-size:7px;line-height:1.55;color:var(--muted)}

/* brand text */
.brand{font-family:var(--head);font-weight:700;color:var(--plum);text-align:center;line-height:1}
.brand__tag{font-family:var(--body);font-size:8px;color:var(--magenta);text-align:center;margin-top:4px;letter-spacing:.1em}

/* about */
.about{background:linear-gradient(180deg,var(--gold-light),var(--gold) 60%,var(--gold-deep))}
.about__inner{position:absolute;inset:0;display:flex;align-items:center;padding:0 34px;gap:26px}
.about__portrait{width:170px;height:170px;border-radius:50%;border:5px solid var(--white);background:radial-gradient(circle at 50% 40%,#8a5a3c,#4a2c1e 70%);flex:none}
.about__heading{font-family:var(--head);font-weight:700;color:var(--plum);font-size:20px;line-height:1.15;margin-bottom:8px}
.about__copy .text-small{color:var(--ink)}
.about__copy .btn{margin-top:10px}

/* services */
.services{background:var(--cream)}
.card-row{display:flex;gap:10px;justify-content:center}
.service-card{width:118px;border-radius:8px;overflow:hidden;background:var(--white);box-shadow:0 2px 6px rgba(0,0,0,.12)}
.service-card__img{height:80px}
.service-card__body{padding:8px;color:var(--white);min-height:78px}
.service-card__name{font-weight:700;font-size:8px;text-transform:uppercase;margin-bottom:4px}
.service-card__body p{font-size:6px;line-height:1.5}
.bg-teal{background:var(--teal)}.bg-green{background:var(--green)}.bg-plum{background:var(--plum)}.bg-magenta{background:var(--magenta)}
.arrow{position:absolute;top:50%;width:18px;height:18px;border-radius:50%;background:var(--gold);color:var(--white);font-size:10px;display:flex;align-items:center;justify-content:center}

/* products */
.products{background:linear-gradient(180deg,var(--plum),var(--magenta))}
.products--light{background:var(--cream)}
.product-card{width:112px;background:var(--white);border-radius:8px;padding:8px;text-align:center;box-shadow:0 2px 6px rgba(0,0,0,.15)}
.product-card__img{height:78px;border-radius:4px;background:linear-gradient(180deg,#f4efe6,#e7d9c3)}
.product-card__name{font-size:6.5px;font-weight:700;color:var(--plum);margin:6px 0 2px;text-transform:uppercase}
.product-card__price{font-size:7px;color:var(--gold-deep);font-weight:700;margin-bottom:5px}

/* why choose */
.why{background:var(--cream)}
.why--plum{background:linear-gradient(180deg,var(--plum),var(--magenta))}
.why__hub{position:absolute;left:50%;width:120px;height:120px;margin-left:-60px;border-radius:50%;background:var(--white);border:6px solid var(--gold);display:flex;flex-direction:column;align-items:center;justify-content:center;box-shadow:0 0 0 6px rgba(138,40,118,.25)}
.why__item{position:absolute;width:150px;display:flex;gap:6px;align-items:flex-start}
.why__icon{flex:none;width:20px;height:20px;border-radius:50%;display:flex;align-items:center;justify-content:center}
.why__label{font-size:7px;font-weight:700;color:var(--plum);text-transform:uppercase;margin-bottom:2px}
.why--plum .why__label{color:var(--white)}
.why--plum .text-small{color:#f1d9ea}

/* blog */
.blog{background:linear-gradient(180deg,var(--gold-light),var(--gold) 50%,var(--gold-deep))}
.blog--light{background:var(--cream)}
.blog-card{width:160px;background:var(--white);border-radius:8px;overflow:hidden;box-shadow:0 2px 6px rgba(0,0,0,.15)}
.blog-card__img{height:90px;background:linear-gradient(135deg,#c99a7a,#8a5a44)}
.blog-card__body{padding:8px}
.blog-card__title{font-size:7px;font-weight:700;color:var(--plum);text-transform:uppercase;margin-bottom:4px}

/* contact */
.contact{background:var(--cream)}
.contact--gold{background:linear-gradient(180deg,var(--gold-light),var(--gold) 55%,var(--gold-deep))}
.contact-form{display:flex;flex-direction:column;gap:6px}
.field{height:18px;background:var(--white);border:1px solid #e2d6c8;border-radius:4px;font-size:6.5px;color:var(--muted);padding:5px 7px}
.field--area{height:44px}
.field-row{display:flex;gap:6px}.field-row .field{flex:1}
.notice{font-size:5.5px;line-height:1.45;color:var(--muted)}

/* footer */
.site-footer{background:linear-gradient(180deg,var(--plum),var(--plum-deep));color:var(--white)}
.footer-cols{display:flex;gap:18px;padding:34px 24px 0}
.footer-col h4{font-size:7px;font-weight:700;letter-spacing:.06em;margin-bottom:6px;text-transform:uppercase}
.footer-col p{font-size:6.5px;line-height:1.7;color:#ecd4e6}
.footer-bar{position:absolute;left:0;right:0;bottom:0;height:20px;background:var(--plum-deep);border-top:1px solid rgba(255,255,255,.2);font-size:6px;color:#e5c8dd;display:flex;align-items:center;justify-content:center}
.brand--light{color:var(--white)}
.brand--light + .brand__tag{color:var(--gold-light)}
</style>
</head>
<body>

<!-- ===== Home layout ===== -->
<main class="page page--home">
  <header class="site-nav">
    <div class="site-nav__contact"><span>&#9742; (916) 555-0142</span><span>&#9993; hello@velvetfern.com</span></div>
    <nav class="site-nav__menu"><span>HOME</span><span>ABOUT</span><span>SERVICES</span><span>SHOP</span><span>BLOG</span><span class="btn btn--small">Book Now</span></nav>
  </header>

  <section class="hero" role="img" aria-label="Spa client relaxing during a facial treatment">
    <div class="hero__text">
      <h1 class="hero__title">REVEAL YOUR<br>NATURAL BEAUTY<br><span class="accent">RESTORE YOUR<br>BALANCE</span></h1>
      <span class="btn">Book Now</span>
    </div>
    <svg class="wave wave--bottom" height="40" viewBox="0 0 568 40" preserveAspectRatio="none"><path d="M0 40 L0 22 Q284 -10 568 22 L568 40Z" fill="#f1cf7a"/><path d="M0 24 Q284 -8 568 24" stroke="#8a2876" stroke-width="3" fill="none"/></svg>
  </section>

  <section class="about" style="height:280px">
    <div class="about__inner">
      <div>
        <div class="about__portrait" role="img" aria-label="Smiling spa guest portrait"></div>
        <div class="brand" style="font-size:15px;margin-top:8px">Velvet Fern</div>
        <div class="brand__tag">Beauty &amp; Balance</div>
      </div>
      <div class="about__copy">
        <h2 class="about__heading">ABOUT<br>VELVET FERN</h2>
        <p class="text-small">Velvet Fern is a body sculpting, facial, waxing and wellness spa where every visit is shaped around you. Our licensed team blends modern techniques with calm, caring rituals.</p>
        <p class="text-small" style="margin-top:6px">We believe true beauty begins with balance, rest and a plan that fits your life.</p>
        <span class="btn btn--plum">Read More</span>
      </div>
    </div>
    <svg class="wave wave--bottom" height="36" viewBox="0 0 568 36" preserveAspectRatio="none"><path d="M0 36 L0 10 Q284 46 568 10 L568 36Z" fill="#fbf6ee"/></svg>
  </section>

  <section class="services" style="height:280px;padding-top:22px">
    <h2 class="section-title" style="margin-bottom:16px">SERVICES OFFERED</h2>
    <div class="card-row">
      <div class="service-card"><div class="service-card__img" style="background:linear-gradient(135deg,#d8b49a,#8c6048)" role="img" aria-label="Body sculpting treatment"></div><div class="service-card__body bg-teal"><div class="service-card__name">Body Sculpting</div><p>Contour and tone with gentle, non-invasive care.</p></div></div>
      <div class="service-card"><div class="service-card__img" style="background:linear-gradient(135deg,#e9cdb8,#a9785c)" role="img" aria-label="Facial treatment"></div><div class="service-card__body bg-green"><div class="service-card__name">Facials</div><p>Deep cleansing rituals for bright, calm skin.</p></div></div>
      <div class="service-card"><div class="service-card__img" style="background:linear-gradient(135deg,#f0d9c6,#b58466)" role="img" aria-label="Waxing service"></div><div class="service-card__body bg-plum"><div class="service-card__name">Waxing</div><p>Smooth results with skin-friendly soft wax.</p></div></div>
      <div class="service-card"><div class="service-card__img" style="background:linear-gradient(135deg,#cfa88c,#7a4e3a)" role="img" aria-label="Wellness massage"></div><div class="service-card__body bg-magenta"><div class="service-card__name">Wellness</div><p>Restore body and mind with holistic care.</p></div></div>
    </div>
    <span class="arrow" style="left:6px">&#8249;</span><span class="arrow" style="right:6px">&#8250;</span>
  </section>

  <section class="products" style="height:300px;padding-top:40px">
    <svg class="wave wave--top" height="30" viewBox="0 0 568 30" preserveAspectRatio="none"><path d="M0 0 L568 0 L568 8 Q284 40 0 8Z" fill="#fbf6ee"/></svg>
    <h2 class="section-title section-title--light" style="margin-bottom:16px">FEATURED PRODUCTS</h2>
    <div class="card-row">
      <div class="product-card"><div class="product-card__img" role="img" aria-label="Cleansing serum bottle"></div><div class="product-card__name">Calming Serum</div><div class="product-card__price">$38.00</div><span class="btn btn--small">Add to Cart</span></div>
      <div class="product-card"><div class="product-card__img" role="img" aria-label="Botanical skin oil"></div><div class="product-card__name">Botanical Oil</div><div class="product-card__price">$42.00</div><span class="btn btn--small">Add to Cart</span></div>
      <div class="product-card"><div class="product-card__img" role="img" aria-label="Amber toner bottle"></div><div class="product-card__name">Glow Toner</div><div class="product-card__price">$29.00</div><span class="btn btn--small">Add to Cart</span></div>
      <div class="product-card"><div class="product-card__img" role="img" aria-label="Body cream jars"></div><div class="product-card__name">Body Cream</div><div class="product-card__price">$34.00</div><span class="btn btn--small">Add to Cart</span></div>
    </div>
    <svg class="wave wave--bottom" height="30" viewBox="0 0 568 30" preserveAspectRatio="none"><path d="M0 30 L0 16 Q284 -12 568 16 L568 30Z" fill="#fbf6ee"/></svg>
  </section>

  <section class="why" style="height:300px;padding-top:16px">
    <h2 class="section-title">WHY CHOOSE VELVET FERN</h2>
    <div class="why__hub" style="top:100px"><div class="brand" style="font-size:13px">Velvet Fern</div><div class="brand__tag" style="font-size:6px">Beauty &amp; Balance</div></div>
    <div class="why__item" style="left:60px;top:90px"><span class="why__icon bg-teal"><svg width="10" height="10" viewBox="0 0 10 10"><path d="M2 5 L4 7 L8 3" stroke="#fff" stroke-width="1.6" fill="none"/></svg></span><div><div class="why__label">Licensed Experts</div><p class="text-small">Certified therapists with years of care.</p></div></div>
    <div class="why__item" style="left:370px;top:90px"><span class="why__icon bg-plum"><svg width="10" height="10" viewBox="0 0 10 10"><path d="M2 5 L4 7 L8 3" stroke="#fff" stroke-width="1.6" fill="none"/></svg></span><div><div class="why__label">Flexible Payment</div><p class="text-small">Pay later plans for every service.</p></div></div>
    <div class="why__item" style="left:60px;top:200px"><span class="why__icon bg-plum"><svg width="10" height="10" viewBox="0 0 10 10"><path d="M2 5 L4 7 L8 3" stroke="#fff" stroke-width="1.6" fill="none"/></svg></span><div><div class="why__label">Holistic Approach</div><p class="text-small">Care for body, skin and mind.</p></div></div>
    <div class="why__item" style="left:370px;top:200px"><span class="why__icon bg-teal"><svg width="10" height="10" viewBox="0 0 10 10"><path d="M2 5 L4 7 L8 3" stroke="#fff" stroke-width="1.6" fill="none"/></svg></span><div><div class="why__label">Secure Intake</div><p class="text-small">Private records, safely stored.</p></div></div>
  </section>

  <section class="blog" style="height:340px;padding-top:40px">
    <svg class="wave wave--top" height="30" viewBox="0 0 568 30" preserveAspectRatio="none"><path d="M0 0 L568 0 L568 8 Q284 40 0 8Z" fill="#fbf6ee"/></svg>
    <h2 class="section-title section-title--light" style="margin-bottom:16px">LATEST BLOG POSTS</h2>
    <div class="card-row">
      <div class="blog-card"><div class="blog-card__img" role="img" aria-label="Facial massage in progress"></div><div class="blog-card__body"><div class="blog-card__title">Your First Facial Guide</div><p class="text-small">What to expect and how to prepare.</p><span class="btn btn--small" style="margin-top:5px">Read More</span></div></div>
      <div class="blog-card"><div class="blog-card__img" role="img" aria-label="Relaxing spa treatment"></div><div class="blog-card__body"><div class="blog-card__title">Sculpting Aftercare Tips</div><p class="text-small">Simple habits for lasting results.</p><span class="btn btn--small" style="margin-top:5px">Read More</span></div></div>
      <div class="blog-card"><div class="blog-card__img" role="img" aria-label="Spa room with candles"></div><div class="blog-card__body"><div class="blog-card__title">Waxing Myths Explained</div><p class="text-small">Facts for smoother, calmer skin.</p><span class="btn btn--small" style="margin-top:5px">Read More</span></div></div>
    </div>
    <svg class="wave wave--bottom" height="30" viewBox="0 0 568 30" preserveAspectRatio="none"><path d="M0 30 L0 14 Q284 -12 568 14 L568 30Z" fill="#fbf6ee"/></svg>
  </section>

  <section class="contact" style="height:260px;display:flex;align-items:center;padding:0 34px;gap:30px">
    <div style="width:220px"><div class="brand" style="font-size:28px">Velvet Fern</div><div class="brand__tag" style="font-size:10px">Beauty &amp; Balance</div></div>
    <div style="flex:1">
      <h2 class="section-title" style="text-align:left;margin-bottom:10px">GET IN TOUCH</h2>
      <div class="contact-form">
        <div class="field-row"><div class="field">Name</div><div class="field">Email</div></div>
        <div class="field">Phone</div>
        <div class="field field--area">Message</div>
        <span class="btn" style="align-self:flex-start">Send Message</span>
        <p class="notice">Please do not share sensitive medical information through this form. Private health details will be collected during your secure, HIPAA-compliant intake process.</p>
      </div>
    </div>
  </section>

  <footer class="site-footer" style="height:140px">
    <svg class="wave wave--top" height="22" viewBox="0 0 568 22" preserveAspectRatio="none"><path d="M0 0 L568 0 L568 4 Q284 30 0 4Z" fill="#fbf6ee"/></svg>
    <div class="footer-cols">
      <div class="footer-col" style="width:120px"><div class="brand brand--light" style="font-size:14px;text-align:left">Velvet Fern</div><div class="brand__tag" style="text-align:left">Beauty &amp; Balance</div></div>
      <div class="footer-col"><h4>Quick Links</h4><p>Home<br>About<br>Services<br>Shop</p></div>
      <div class="footer-col"><h4>Contact Info</h4><p>2180 Alder Row<br>Sacramento, CA 95731<br>(916) 555-0142</p></div>
      <div class="footer-col"><h4>Newsletter</h4><p>Tips and offers monthly.</p><span class="btn btn--small" style="margin-top:4px">Subscribe</span></div>
    </div>
    <div class="footer-bar">&copy; 2025 Velvet Fern. All rights reserved.</div>
  </footer>
</main>

<!-- ===== Alternate layout ===== -->
<main class="page page--alt">
  <header class="site-nav">
    <div class="site-nav__contact"><span>&#9742; (916) 555-0142</span><span>&#9993; hello@velvetfern.com</span></div>
    <nav class="site-nav__menu"><span>HOME</span><span>ABOUT</span><span>SERVICES</span><span>SHOP</span><span>BLOG</span><span class="btn btn--small">Book Now</span></nav>
  </header>

  <section class="hero" role="img" aria-label="Guest enjoying a relaxing facial">
    <div class="hero__text">
      <h1 class="hero__title">REVEAL YOUR<br>NATURAL BEAUTY<br><span class="accent">RESTORE YOUR<br>BALANCE</span></h1>
      <span class="btn">Book Now</span>
    </div>
    <svg class="wave wave--bottom" height="40" viewBox="0 0 568 40" preserveAspectRatio="none"><path d="M0 40 L0 22 Q284 -10 568 22 L568 40Z" fill="#ffffff"/><path d="M0 24 Q284 -8 568 24" stroke="#d9a23a" stroke-width="3" fill="none"/></svg>
  </section>

  <section style="height:240px;background:var(--white);display:flex;align-items:center;padding:0 34px;gap:30px">
    <div style="width:210px"><div class="brand" style="font-size:26px">Velvet Fern</div><div class="brand__tag" style="font-size:10px">Beauty &amp; Balance</div></div>
    <div class="about__copy" style="flex:1">
      <h2 class="about__heading">ABOUT<br>VELVET FERN</h2>
      <p class="text-small">Velvet Fern is a body sculpting, facial, waxing and wellness spa where every visit is shaped around you. Our team blends modern methods with calm rituals.</p>
      <span class="btn btn--plum">Read More</span>
    </div>
  </section>

  <section class="about" style="height:320px;padding-top:44px">
    <svg class="wave wave--top" height="30" viewBox="0 0 568 30" preserveAspectRatio="none"><path d="M0 0 L568 0 L568 8 Q284 40 0 8Z" fill="#ffffff"/></svg>
    <h2 class="section-title" style="margin-bottom:16px">SERVICES OFFERED</h2>
    <div class="card-row" style="gap:14px">
      <div class="service-card" style="width:140px"><div class="service-card__img" style="height:90px;background:linear-gradient(135deg,#d8b49a,#8c6048)" role="img" aria-label="Body sculpting treatment"></div><div class="service-card__body bg-plum"><div class="service-card__name">Body Sculpting</div><p>Contour and tone with gentle care.</p></div></div>
      <div class="service-card" style="width:140px"><div class="service-card__img" style="height:90px;background:linear-gradient(135deg,#e9cdb8,#a9785c)" role="img" aria-label="Facial treatment"></div><div class="service-card__body bg-teal"><div class="service-card__name">Facials</div><p>Deep cleansing for bright skin.</p></div></div>
      <div class="service-card" style="width:140px"><div class="service-card__img" style="height:90px;background:linear-gradient(135deg,#cfa88c,#7a4e3a)" role="img" aria-label="Wellness massage"></div><div class="service-card__body bg-magenta"><div class="service-card__name">Wellness</div><p>Holistic care for body and mind.</p></div></div>
    </div>
    <span class="arrow" style="left:8px">&#8249;</span><span class="arrow" style="right:8px">&#8250;</span>
    <svg class="wave wave--bottom" height="30" viewBox="0 0 568 30" preserveAspectRatio="none"><path d="M0 30 L0 14 Q284 -12 568 14 L568 30Z" fill="#8a2876"/></svg>
  </section>

  <section class="why why--plum" style="height:320px;padding-top:16px">
    <h2 class="section-title section-title--light">WHY CHOOSE VELVET FERN</h2>
    <div class="why__hub" style="top:110px"><div class="brand" style="font-size:13px">Velvet Fern</div><div class="brand__tag" style="font-size:6px">Beauty &amp; Balance</div></div>
    <div class="why__item" style="left:60px;top:70px"><span class="why__icon bg-teal"><svg width="10" height="10" viewBox="0 0 10 10"><path d="M2 5 L4 7 L8 3" stroke="#fff" stroke-width="1.6" fill="none"/></svg></span><div><div class="why__label">Licensed Experts</div><p class="text-small">Certified, caring therapists.</p></div></div>
    <div class="why__item" style="left:370px;top:70px"><span class="why__icon" style="background:var(--gold)"><svg width="10" height="10" viewBox="0 0 10 10"><path d="M2 5 L4 7 L8 3" stroke="#fff" stroke-width="1.6" fill="none"/></svg></span><div><div class="why__label">Flexible Payment</div><p class="text-small">Pay later plans available.</p></div></div>
    <div class="why__item" style="left:40px;top:180px"><span class="why__icon" style="background:var(--gold)"><svg width="10" height="10" viewBox="0 0 10 10"><path d="M2 5 L4 7 L8 3" stroke="#fff" stroke-width="1.6" fill="none"/></svg></span><div><div class="why__label">Holistic Approach</div><p class="text-small">Body, skin and mind.</p></div></div>
    <div class="why__item" style="left:390px;top:180px"><span class="why__icon bg-teal"><svg width="10" height="10" viewBox="0 0 10 10"><path d="M2 5 L4 7 L8 3" stroke="#fff" stroke-width="1.6" fill="none"/></svg></span><div><div class="why__label">Secure Intake</div><p class="text-small">Private records kept safe.</p></div></div>
    <div class="why__item" style="left:220px;top:262px;width:140px"><span class="why__icon bg-teal"><svg width="10" height="10" viewBox="0 0 10 10"><path d="M2 5 L4 7 L8 3" stroke="#fff" stroke-width="1.6" fill="none"/></svg></span><div><div class="why__label">Results Driven</div><p class="text-small">Plans built around you.</p></div></div>
  </section>

  <section class="products products--light" style="height:220px;padding-top:18px">
    <h2 class="section-title" style="margin-bottom:14px">FEATURED PRODUCTS</h2>
    <div class="card-row">
      <div class="product-card"><div class="product-card__img" style="height:66px" role="img" aria-label="Cleansing serum bottle"></div><div class="product-card__name">Calming Serum</div><div class="product-card__price">$38.00</div><span class="btn btn--small">Add to Cart</span></div>
      <div class="product-card"><div class="product-card__img" style="height:66px" role="img" aria-label="Botanical skin oil"></div><div class="product-card__name">Botanical Oil</div><div class="product-card__price">$42.00</div><span class="btn btn--small">Add to Cart</span></div>
      <div class="product-card"><div class="product-card__img" style="height:66px" role="img" aria-label="Amber toner bottle"></div><div class="product-card__name">Glow Toner</div><div class="product-card__price">$29.00</div><span class="btn btn--small">Add to Cart</span></div>
      <div class="product-card"><div class="product-card__img" style="height:66px" role="img" aria-label="Body cream jars"></div><div class="product-card__name">Body Cream</div><div class="product-card__price">$34.00</div><span class="btn btn--small">Add to Cart</span></div>
    </div>
  </section>

  <section class="contact contact--gold" style="height:260px;padding:42px 90px 0">
    <svg class="wave wave--top" height="30" viewBox="0 0 568 30" preserveAspectRatio="none"><path d="M0 0 L568 0 L568 8 Q284 40 0 8Z" fill="#fbf6ee"/></svg>
    <h2 class="section-title" style="margin-bottom:10px">GET IN TOUCH</h2>
    <div class="contact-form">
      <div class="field-row"><div class="field">Name</div><div class="field">Email</div></div>
      <div class="field field--area">Message</div>
      <span class="btn btn--plum" style="align-self:center">Send Message</span>
      <p class="notice" style="color:var(--ink);text-align:center">Please do not share sensitive medical information through this form. Private health details will be collected during your secure, HIPAA-compliant intake process.</p>
    </div>
    <svg class="wave wave--bottom" height="30" viewBox="0 0 568 30" preserveAspectRatio="none"><path d="M0 30 L0 14 Q284 -12 568 14 L568 30Z" fill="#fbf6ee"/></svg>
  </section>

  <section class="blog blog--light" style="height:320px;padding-top:18px">
    <h2 class="section-title" style="margin-bottom:16px">LATEST BLOG POSTS</h2>
    <div style="display:flex;gap:14px;padding:0 40px">
      <div class="blog-card" style="width:230px"><div class="blog-card__img" style="height:150px" role="img" aria-label="Facial massage in progress"></div><div class="blog-card__body"><div class="blog-card__title">Your First Facial Guide</div><p class="text-small">What to expect and how to prepare.</p><span class="btn btn--small" style="margin-top:5px">Read More</span></div></div>
      <div style="flex:1;display:flex;flex-direction:column;gap:12px">
        <div style="display:flex;gap:8px;align-items:center"><div class="photo" style="width:90px;height:70px;background:linear-gradient(135deg,#c99a7a,#8a5a44)" role="img" aria-label="Relaxing spa treatment"></div><div><div class="blog-card__title">Sculpting Aftercare Tips</div><p class="text-small">Simple habits for lasting results.</p></div></div>
        <div style="display:flex;gap:8px;align-items:center"><div class="photo" style="width:90px;height:70px;background:linear-gradient(135deg,#dcb89a,#9a6a50)" role="img" aria-label="Spa room with candles"></div><div><div class="blog-card__title">Waxing Myths Explained</div><p class="text-small">Facts for smoother, calmer skin.</p></div></div>
        <div style="display:flex;gap:8px;align-items:center"><div class="photo" style="width:90px;height:70px;background:linear-gradient(135deg,#d0a080,#7e4e38)" role="img" aria-label="Wellness session"></div><div><div class="blog-card__title">Balance at Home</div><p class="text-small">Daily rituals for calm and glow.</p></div></div>
      </div>
    </div>
  </section>

  <footer class="site-footer" style="height:240px">
    <svg class="wave wave--top" height="22" viewBox="0 0 568 22" preserveAspectRatio="none"><path d="M0 0 L568 0 L568 4 Q284 30 0 4Z" fill="#fbf6ee"/></svg>
    <div class="footer-cols" style="padding-top:44px">
      <div class="footer-col" style="width:120px"><div class="brand brand--light" style="font-size:16px;text-align:left">Velvet Fern</div><div class="brand__tag" style="text-align:left">Beauty &amp; Balance</div></div>
      <div class="footer-col"><h4>Quick Links</h4><p>Home<br>About<br>Services<br>Shop<br>Blog</p></div>
      <div class="footer-col"><h4>Contact Info</h4><p>2180 Alder Row<br>Sacramento, CA 95731<br>(916) 555-0142<br>hello@velvetfern.com</p></div>
      <div class="footer-col"><h4>Newsletter</h4><p>Tips and offers monthly.</p><div class="field" style="margin-top:4px;width:110px">Your email</div><span class="btn btn--small" style="margin-top:4px">Subscribe</span></div>
    </div>
    <div class="footer-bar">&copy; 2025 Velvet Fern. All rights reserved.</div>
  </footer>
</main>

</body>
</html>
```